Film Poster: a short documentary about the father of Arabian Racing Horses

NOTE: PLEASE ONLY USE ATTACHED PICTURE

I'd like to design a film poster for my upcoming short documentary to use as part of the marketing material. The film captures the story of a legendary Arabian racing horse, who later become the most influential stallion producing hunderes of champion horses. The film title is "Zafir: Tale of the Dunes".

I'd like to receive the .psd file to be able to add any festival/awards logos later on as I apply the film to film festivals.

Industry/Entity Type

Film Production

Requirements
Must have
• I'd love the poster to include both Arabic and English titles and they are:
• English: Zafir: Tale of the Dunes
• Arabic: ظافر: حكاية الكثبان الذهبية
• I'd also like to poster to include the classical credits at the bottom of the poster that includes the following information:
• In Association with KESTREL PICTURE GUILD
• Supported by KPG QATAR MOVIE TRUST
• Directed by HAMAD ALSUWAIDEN
• Produced by HAMAD ALSUWAIDEN and TOM GARLAND
• Executive Producer RANIA SAFFOURI
• Cinematography PETER MORLEY
• Sound KARIM DOUBARI
• Editing MUSTAFA QIRBANI and TARIQ ALSHANFARI
Nice to have
• The colours of the horse's team is maroon and white, and it would be nice if I can have a touch of those two colours in the design maybe as a splash on the side or to lines crossing horizontally.

```html
<!DOCTYPE html>
<html lang="en">
<head>
<meta charset="utf-8">
<title>Zafir: Tale of the Dunes — Poster</title>
<link rel="stylesheet" href="https://fonts.googleapis.com/css2?family=Raleway:wght@300;400&family=Cinzel:wght@400&family=Cairo:wght@300&family=Oswald:wght@300;400&display=swap">
<style>
  :root {
    --maroon: #7b1418;
    --maroon-deep: #5a0b10;
    --maroon-light: #8e1d21;
    --paper: #d9d9d7;
    --paper-light: #ecebe9;
    --coat-dark: #7f7f80;
    --coat-mid: #a7a7a7;
    --coat-light: #dcdcda;
    --title-white: #f4f1ee;
    --arabic-grey: #d6cfcc;
    --credit-ink: #3d3d3d;
  }
  html, body {
    margin: 0;
    padding: 0;
    width: 800px;
    height: 1200px;
    overflow: hidden;
    background: var(--paper);
  }
  .poster {
    position: relative;
    width: 800px;
    height: 1200px;
    overflow: hidden;
    background:
      radial-gradient(ellipse 500px 180px at 30% 1080px, rgba(255,255,255,0.35), transparent 70%),
      linear-gradient(180deg, var(--paper-light) 0%, var(--paper) 100%);
  }
  .hero-photo {
    position: absolute;
    left: 0; top: 0;
    width: 800px; height: 620px;
    background:
      radial-gradient(ellipse 260px 340px at 22% 35%, rgba(110,110,112,0.55), transparent 70%),
      radial-gradient(ellipse 300px 260px at 88% 30%, rgba(235,235,233,0.7), transparent 70%),
      linear-gradient(125deg, transparent 38%, rgba(70,70,72,0.35) 52%, transparent 66%),
      linear-gradient(100deg, var(--coat-dark) 0%, var(--coat-mid) 40%, #c3c3c1 68%, var(--coat-light) 100%);
  }
  .title-band {
    position: absolute;
    left: 0; top: 0;
    width: 800px; height: 1200px;
  }
  .title-block {
    position: absolute;
    left: 0; right: 0;
    text-align: center;
    color: var(--title-white);
  }
  .title-main {
    top: 654px;
    margin: 0;
    font-family: 'Raleway', sans-serif;
    font-weight: 400;
    font-size: 50px;
    letter-spacing: 13px;
    padding-left: 13px;
    line-height: 1;
  }
  .title-sub {
    top: 738px;
    margin: 0;
    font-family: 'Cinzel', serif;
    font-size: 23px;
    letter-spacing: 8.5px;
    padding-left: 8px;
    line-height: 1;
  }
  .title-arabic {
    top: 816px;
    margin: 0;
    font-family: 'Cairo', sans-serif;
    font-weight: 300;
    font-size: 34px;
    color: var(--arabic-grey);
    line-height: 1.3;
  }
  .credits {
    position: absolute;
    left: 0; right: 0;
    top: 1052px;
    text-align: center;
    font-family: 'Oswald', sans-serif;
    font-weight: 400;
    color: var(--credit-ink);
    text-transform: uppercase;
  }
  .credit-line {
    margin: 0 0 10px;
    font-size: 16px;
    letter-spacing: 0.2px;
    line-height: 24px;
    white-space: nowrap;
  }
  .credit-line .role {
    font-size: 9.5px;
    font-weight: 300;
    letter-spacing: 0.3px;
    margin: 0 2px;
  }
</style>
</head>
<body>
<main class="poster">
  <div class="hero-photo" role="img" aria-label="Close-up photograph of a grey Arabian horse wearing a leather halter with a brass nameplate"></div>

  <svg class="title-band" viewBox="0 0 800 1200" aria-hidden="true">
    <defs>
      <filter id="brush-edge" x="-5%" y="-10%" width="110%" height="120%">
        <feTurbulence type="fractalNoise" baseFrequency="0.09 0.045" numOctaves="3" seed="7" result="noise"/>
        <feDisplacementMap in="SourceGraphic" in2="noise" scale="22" xChannelSelector="R" yChannelSelector="G"/>
      </filter>
      <linearGradient id="band-shade" x1="0" y1="0" x2="1" y2="1">
        <stop offset="0" stop-color="var(--maroon-deep)"/>
        <stop offset="0.5" stop-color="var(--maroon)"/>
        <stop offset="1" stop-color="var(--maroon-light)"/>
      </linearGradient>
    </defs>
    <g filter="url(#brush-edge)">
      <path fill="url(#band-shade)" d="M0,530 L8,522 14,538 22,526 30,545 42,540 48,552 58,544 66,556 80,548 92,560 104,552 118,566 130,558 142,570 156,562 170,574 182,566 196,578 210,570 224,582 236,574 250,585 262,576 276,586 290,578 304,584 316,572 330,580 344,570 358,578 372,568 386,575 400,566 414,572 428,562 442,570 456,560 470,566 484,556 498,562 512,552 526,558 540,548 554,552 566,540 578,548 590,536 604,544 616,530 628,540 640,528 652,536 664,524 676,534 688,522 700,532 712,518 724,528 734,512 742,526 752,514 762,522 770,508 778,520 788,510 800,516 L800,930 792,946 784,936 776,958 766,944 756,962 744,950 732,968 720,954 708,972 696,958 684,978 672,960 660,974 648,956 636,970 624,952 612,966 600,950 588,964 576,946 564,962 552,948 540,966 528,950 516,968 504,952 492,970 480,954 468,972 456,956 444,974 432,958 420,976 408,960 396,978 384,962 372,980 360,964 348,982 336,966 324,984 312,968 300,986 288,970 276,980 264,962 252,976 240,958 228,972 216,956 204,970 192,954 180,968 168,950 156,966 144,948 132,964 120,946 108,962 96,944 84,960 72,942 60,958 48,940 36,956 24,938 12,952 0,940 Z"/>
      <circle cx="762" cy="500" r="4" fill="var(--maroon)"/>
      <circle cx="744" cy="506" r="2.5" fill="var(--maroon)"/>
      <circle cx="50" cy="968" r="3" fill="var(--maroon)"/>
      <circle cx="310" cy="996" r="2.5" fill="var(--maroon)"/>
      <circle cx="690" cy="988" r="3" fill="var(--maroon)"/>
    </g>
  </svg>

  <h1 class="title-block title-main">ZAFIR</h1>
  <p class="title-block title-sub">TALE OF THE DUNES</p>
  <p class="title-block title-arabic" lang="ar" dir="rtl">ظافر: حكاية الكثبان الذهبية</p>

  <section class="credits">
    <p class="credit-line"><span class="role">In association with</span> KESTREL PICTURE GUILD <span class="role">supported by</span> KPG QATAR MOVIE TRUST "ZAFIR"</p>
    <p class="credit-line"><span class="role">Edited by</span> MUSTAFA QIRBANI <span class="role">and</span> TARIQ ALSHANFARI <span class="role">Sound design by</span> KARIM DOUBARI <span class="role">Director of photography</span> PETER MORLEY</p>
    <p class="credit-line"><span class="role">Executive producer</span> RANIA SAFFOURI <span class="role">Produced by</span> HAMAD ALSUWAIDEN <span class="role">and</span> TOM GARLAND <span class="role">Directed by</span> HAMAD ALSUWAIDEN</p>
  </section>
</main>
</body>
</html>
```